Save the date: email notification

I need a "Save the Date" email notification design for my wedding:

Objetives:

1.- to notify friends about our future wedding ( by sending an email)
2.- to request our friends to send us their phisical address. ( reply to the email)

It will not be the formal invitation for the wedding, just an announcement.

Wedding Date: 15-sep-2012
Our names: Lucía & Rodrigo

Target Market(s)

friends, family and other commitments

Industry/Entity Type

Wedding

Requirements
Must have
• Wedding Date: 15-sep-2012
Our names: Lucía & Rodrigo

```html
<!DOCTYPE html>
<html lang="en">
<head>
<meta charset="utf-8">
<title>Save the Date – Lucía &amp; Rodrigo</title>
<link rel="stylesheet" href="https://fonts.googleapis.com/css2?family=Felipa&display=swap">
<style>
  :root {
    --paper-pink: #e6a9bb;
    --paper-stripe: #e19fb3;
    --ornament-grey: #9a9a98;
    --card-white: #fdf9fb;
    --ink-violet: #7b5cc6;
    --ink-rose: #ddabc0;
  }
  * { margin: 0; padding: 0; box-sizing: border-box; }
  html, body { width: 1200px; height: 851px; overflow: hidden; }
  body {
    position: relative;
    background-color: var(--paper-pink);
    background-image: repeating-linear-gradient(90deg, var(--paper-pink) 0 4px, var(--paper-stripe) 4px 6px);
    font-family: "Felipa", "Lucida Calligraphy", cursive;
  }
  .ornament { position: absolute; display: block; }
  .ornament--top-right { left: 560px; top: 0; width: 640px; height: 430px; }
  .ornament--bottom-left { left: 0; top: 430px; width: 640px; height: 421px; }
  .announcement {
    position: absolute;
    left: 118px; top: 101px;
    width: 964px; height: 646px;
    background: var(--card-white);
    text-align: center;
  }
  .announcement p { position: absolute; left: 0; right: 0; white-space: nowrap; font-style: italic; line-height: 1; }
  .couple-names { top: 32px; font-size: 80px; color: var(--ink-violet); }
  .announcement-line { font-size: 50px; color: var(--ink-rose); letter-spacing: 1px; }
  .announcement-line--first { top: 150px; }
  .announcement-line--second { top: 214px; }
  .wedding-day { top: 302px; font-size: 66px; color: var(--ink-violet); }
  .wedding-date { top: 398px; font-size: 82px; color: var(--ink-violet); letter-spacing: 1px; }
  .rsvp-line { font-size: 38px; color: var(--ink-rose); letter-spacing: 1px; }
  .rsvp-line--first { top: 536px; }
  .rsvp-line--second { top: 582px; }
</style>
</head>
<body>
  <svg class="ornament ornament--top-right" viewBox="0 0 640 430" role="img" aria-label="Grey stencilled rose and leaf ornament">
    <defs>
      <radialGradient id="roseGlowTop" cx="0.78" cy="0.22" r="0.7">
        <stop offset="0" stop-color="#9a9a98" stop-opacity="0.75"/>
        <stop offset="1" stop-color="#9a9a98" stop-opacity="0"/>
      </radialGradient>
    </defs>
    <rect width="640" height="430" fill="url(#roseGlowTop)"/>
  </svg>
  <svg class="ornament ornament--bottom-left" viewBox="0 0 640 421" role="img" aria-label="Grey stencilled rose and leaf ornament">
    <defs>
      <radialGradient id="roseGlowBottom" cx="0.2" cy="0.78" r="0.7">
        <stop offset="0" stop-color="#9a9a98" stop-opacity="0.75"/>
        <stop offset="1" stop-color="#9a9a98" stop-opacity="0"/>
      </radialGradient>
    </defs>
    <rect width="640" height="421" fill="url(#roseGlowBottom)"/>
  </svg>

  <main class="announcement">
    <p class="couple-names">Lucía &amp; Rodrigo</p>
    <p class="announcement-line announcement-line--first">Would like to announce thier</p>
    <p class="announcement-line announcement-line--second">forth coming wedding.</p>
    <p class="wedding-day">Saturday</p>
    <p class="wedding-date">15th September 2012</p>
    <p class="rsvp-line rsvp-line--first">Please R.S.V.P. via email</p>
    <p class="rsvp-line rsvp-line--second">with your full postal address.</p>
  </main>
</body>
</html>
```